Moden - Mexicali - Flower Shop

brisapetals is looking for a cool web design that has a airy, clean, mexicali feel to it.

See attached images and links for idea of what we mean with the above.

please no templates.
Updates

Target Market(s)

Local flower shop in San Diego, California

Industry/Entity Type

Shop

Requirements
Must have
• see. brisapetals.quillcart.example - I did the site and logo...I love the logo - hate the site.

Going for this feel: http://www.plumnotebook.example/tablecraft/archives/verandos.php

I also attached another site I liked- I just feel like it may be to busy.

```html
<!DOCTYPE html>
<html lang="en">
<head>
<meta charset="utf-8">
<title>Brisa Petals – Online Flower Shop</title>
<link href="https://fonts.googleapis.com/css2?family=Oxygen:wght@300;400;700&family=Open+Sans:wght@400;600&display=swap" rel="stylesheet">
<style>
:root{
  --ink:#2b2b2b;
  --text:#555;
  --muted:#8a8a8a;
  --line:#d9d9d9;
  --accent:#6cbfa5;
  --brand:#7fb8b0;
  --chalk-text:#e8e8e8;
  --submit:#35aee3;
  --card-border:#e3e3e3;
}
*{box-sizing:border-box;margin:0;padding:0}
html,body{width:1200px;height:2256px;overflow:hidden;background:#fff}
body{position:relative;font-family:"Oxygen",sans-serif;color:var(--text)}
a{color:inherit;text-decoration:none}
.abs{position:absolute}

.top-rule{left:87px;width:1026px;top:0;height:4px;background:var(--ink)}
.account-links{left:98px;top:29px;font-size:13px;color:var(--muted)}
.account-links span{margin:0 6px}
.search{left:693px;top:21px;width:259px;height:36px;border:1px solid #e6e6e6;font-size:13px;color:#999;padding:9px 12px}
.search svg{position:absolute;right:10px;top:10px}
.cart{left:1022px;top:26px;font-size:13px;color:var(--muted);display:flex;align-items:center;gap:8px}
.wavy{left:87px;width:1026px;height:6px;border-top:2px dotted #cfcfcf}

.brand{left:0;width:1200px;top:112px;height:60px;line-height:60px;text-align:center;font-family:"Oxygen",sans-serif;font-weight:300;font-size:46px;letter-spacing:3px;color:var(--brand)}

.main-nav{left:87px;width:1026px;top:204px;height:60px;border-top:2px solid #b5b5b5;border-bottom:4px solid var(--ink);display:flex;align-items:center}
.main-nav a{font-size:18px;font-weight:300;color:#4a4a4a;padding:0 28px;border-left:1px solid #cfcfcf;line-height:28px}
.main-nav .home{border-left:none;padding:0 40px 0 44px}

.hero{left:87px;top:290px;width:1026px;height:483px;background:linear-gradient(100deg,#e9ebe4 0%,#cfd7c8 16%,#efa58d 30%,#f3b79e 45%,#b0836a 62%,#8e6a50 80%,#b89e80 100%);overflow:hidden}
.hero-copy{left:503px;top:162px;width:498px;text-align:center;color:#fff}
.hero-kicker{font-size:16px;letter-spacing:1px}
.hero-sep{margin:12px auto 10px;width:170px;height:1px;background:rgba(255,255,255,.7)}
.hero-title{font-size:34px;font-weight:400;letter-spacing:.5px;white-space:nowrap}
.hero-text{font-size:14px;line-height:26px;margin-top:6px}
.hero-btn{display:inline-block;margin-top:20px;border:1px solid #fff;padding:7px 22px;font-size:16px}
.hero-arrow{top:218px;width:38px;height:74px}

.welcome-title{left:40px;width:335px;top:840px;text-align:right;font-size:30px;line-height:44px;font-weight:300;color:#444;white-space:nowrap}
.welcome-title em{font-style:normal;color:var(--accent)}
.welcome-text{left:424px;width:689px;top:843px;font-size:13.5px;line-height:27px;color:#666}

.tabs{left:87px;width:1026px;top:986px;height:26px;display:flex;align-items:center}
.tabs .rule{flex:1;height:2px;background:#444}
.tabs .dot{width:7px;height:7px;border-radius:50%;background:#222;margin:0 12px}
.tabs span{font-size:17px;letter-spacing:2px;color:#333}
.tabs .inactive{color:var(--muted)}
.pager{top:1040px;left:537px;display:flex;gap:6px}
.pager a{height:25px;width:62px;color:#fff;font-size:12px;display:flex;align-items:center;justify-content:center;background:#111}
.pager .prev{clip-path:polygon(14% 0,100% 0,100% 100%,14% 100%,0 50%)}
.pager .next{clip-path:polygon(0 0,86% 0,100% 50%,86% 100%,0 100%)}

.products{left:87px;top:1117px;width:1026px;display:grid;grid-template-columns:repeat(4,221px);column-gap:47px;row-gap:50px}
.product{height:309px;border:2px solid var(--card-border);text-align:center;font-family:"Open Sans",sans-serif}
.product-photo{width:184px;height:174px;margin:14px auto 0;border-radius:2px}
.product-name{margin-top:20px;font-size:15px;font-weight:400;color:#333}
.product-price{margin-top:14px;font-size:16px;font-weight:600;color:#222}
.stars{margin-top:6px;letter-spacing:2px;font-size:11px;color:#bbb}

.footer{left:0;top:1857px;width:1200px;height:399px;background:radial-gradient(ellipse at 50% 40%,#4a4a4a,#333 80%);color:var(--chalk-text)}
.f-col h3{font-weight:400;font-size:27px;color:#fff;margin-bottom:16px}
.f-col p{font-size:13.5px;line-height:27px}
.meet{left:87px;top:52px;width:310px}
.reach{left:514px;top:52px;width:260px}
.reach li{list-style:none;display:flex;gap:20px;font-size:13.5px;line-height:27px;margin-bottom:18px}
.reach svg{flex:none;margin-top:6px}
.newsletter{left:827px;top:52px;width:290px}
.subscribe{display:flex;margin-top:24px}
.subscribe input{width:197px;height:38px;border:none;background:#e8e8e8}
.subscribe button{width:87px;height:38px;border:none;background:var(--submit);color:#fff;font-family:"Oxygen",sans-serif;font-size:15px;font-weight:700}
.social{left:87px;top:210px;display:flex;gap:14px}
.social span{width:42px;height:42px;border-radius:50%;background:#fff}
.f-wavy{left:87px;top:302px;width:1026px;border-top:2px dotted #777}
.f-links{left:92px;top:343px;font-size:13.5px}
.f-copy{right:92px;top:343px;font-size:13.5px}
</style>
</head>
<body>

<div class="abs top-rule"></div>
<nav class="abs account-links"><a href="#">Register</a><span>|</span><a href="#">Login</a><span>|</span><a href="#">My Account</a></nav>
<div class="abs search">Search
  <svg width="14" height="14" viewBox="0 0 14 14"><circle cx="6" cy="6" r="4.5" fill="none" stroke="#999" stroke-width="1.6"/><line x1="9.3" y1="9.3" x2="13" y2="13" stroke="#999" stroke-width="1.8"/></svg>
</div>
<div class="abs cart">
  <svg width="24" height="20" viewBox="0 0 24 20"><path d="M1 2h4l3 11h12l3-8H7" fill="none" stroke="#333" stroke-width="2"/><circle cx="9" cy="17" r="1.8" fill="#333"/><circle cx="18" cy="17" r="1.8" fill="#333"/></svg>
  Items (0)
</div>
<div class="abs wavy" style="top:78px"></div>

<header class="abs brand">Brisa Petals</header>

<nav class="abs main-nav">
  <a class="home" href="#"><svg width="30" height="26" viewBox="0 0 30 26"><path d="M15 1 1 13h4v12h8v-8h4v8h8V13h4z" fill="#222"/></svg></a>
  <a href="#">OUR SHOP</a><a href="#">FRESH THIS WEEK</a><a href="#">CURATED COLLECTIONS</a><a href="#">BLOG</a><a href="#" style="padding-right:0">CONTACT US</a>
</nav>

<section class="abs hero" role="img" aria-label="Bouquet of white daisies, pink roses and purple blooms on a rustic wooden table">
  <div class="abs hero-copy">
    <div class="hero-kicker">CONSEQUAT IPMNC</div>
    <div class="hero-sep"></div>
    <h2 class="hero-title">OFFER OF THE WEEK</h2>
    <p class="hero-text">Claritas est etiam processus dynamicus, qui sequitur mutationem consuetudium lectorum. Mirum est notare quam littera gothica, quam nunc</p>
    <a class="hero-btn" href="#">SHOP NOW</a>
  </div>
  <svg class="abs hero-arrow" style="left:0" viewBox="0 0 38 74"><path d="M0 0 38 37 0 74z" fill="#fff"/><path d="M10 30 4 37l6 7" fill="none" stroke="#555" stroke-width="1.5"/></svg>
  <svg class="abs hero-arrow" style="right:0" viewBox="0 0 38 74"><path d="M38 0 0 37l38 37z" fill="#fff"/><path d="M28 30l6 7-6 7" fill="none" stroke="#555" stroke-width="1.5"/></svg>
</section>

<h1 class="abs welcome-title">WELCOME TO<br>OUR <em>ONLINE STORE</em></h1>
<p class="abs welcome-text">Duis autem vel eum iriure dolor in hendrerit in vulputate velit esse molestie consequat, vel illum dolore eu feugiat nulla facilisis at vero eros et accumsan et iusto. Nam liber tempor cum soluta nobis eleifend option congue nihil imperdiet doming. Nam liber tempor cum soluta nobis eleifend option congue nihil imperdiet.</p>

<div class="abs tabs"><div class="rule"></div><i class="dot"></i><span>FRESH THIS WEEK</span><i class="dot"></i><span class="inactive">CURATED COLLECTIONS</span><i class="dot"></i><div class="rule"></div></div>
<div class="abs pager"><a class="prev" href="#">prev</a><a class="next" href="#">next</a></div>

<section class="abs products">
  <article class="product"><div class="product-photo" role="img" aria-label="Pink and white bouquet in a polka-dot box" style="background:radial-gradient(circle at 50% 40%,#e7779f,#f4e4ec 70%,#fafafa)"></div><h4 class="product-name">Beciegast nveriti vaert</h4><p class="product-price">$119.50</p><p class="stars">☆☆☆☆☆</p></article>
  <article class="product"><div class="product-photo" role="img" aria-label="Yellow and orange lilies in a glass vase" style="background:radial-gradient(circle at 50% 40%,#f2c637,#f4ecc9 70%,#fafafa)"></div><h4 class="product-name">Beciegast nveriti vaert</h4><p class="product-price">$119.50</p><p class="stars">☆☆☆☆☆</p></article>
  <article class="product"><div class="product-photo" role="img" aria-label="Pink lilies and roses in a square glass vase" style="background:radial-gradient(circle at 50% 40%,#d9467e,#f3dce6 70%,#fafafa)"></div><h4 class="product-name">Beciegast nveriti vaert</h4><p class="product-price">$119.50</p><p class="stars">☆☆☆☆☆</p></article>
  <article class="product"><div class="product-photo" role="img" aria-label="Yellow and purple bouquet in a clear vase" style="background:radial-gradient(circle at 50% 40%,#e9cf2a,#8a5fb0 45%,#ece8f2 72%,#fafafa)"></div><h4 class="product-name">Beciegast nveriti vaert</h4><p class="product-price">$119.50</p><p class="stars">☆☆☆☆☆</p></article>
  <article class="product"><div class="product-photo" role="img" aria-label="Purple and green arrangement in a lavender cube" style="background:radial-gradient(circle at 50% 40%,#a16bbf,#b8d77a 45%,#eef2e6 72%,#fafafa)"></div><h4 class="product-name">Beciegast nveriti vaert</h4><p class="product-price">$119.50</p><p class="stars">☆☆☆☆☆</p></article>
  <article class="product"><div class="product-photo" role="img" aria-label="Pink roses and lilac blooms in a glass vase" style="background:radial-gradient(circle at 50% 40%,#e59cc4,#efe1ef 70%,#fafafa)"></div><h4 class="product-name">Beciegast nveriti vaert</h4><p class="product-price">$119.50</p><p class="stars">☆☆☆☆☆</p></article>
  <article class="product"><div class="product-photo" role="img" aria-label="Orange and red lilies in a tall glass vase" style="background:radial-gradient(circle at 50% 40%,#ee8a35,#f3e2cf 70%,#fafafa)"></div><h4 class="product-name">Beciegast nveriti vaert</h4><p class="product-price">$119.50</p><p class="stars">☆☆☆☆☆</p></article>
  <article class="product"><div class="product-photo" role="img" aria-label="Yellow lilies and pink blooms in a pink vase" style="background:radial-gradient(circle at 50% 40%,#f0d43a,#e8609a 50%,#f5e6ee 72%,#fafafa)"></div><h4 class="product-name">Beciegast nveriti vaert</h4><p class="product-price">$119.50</p><p class="stars">☆☆☆☆☆</p></article>
</section>

<footer class="abs footer">
  <div class="abs f-col meet">
    <h3>Meet Brisa</h3>
    <p>Based in Hillcrest, San Diego - We offer farm fresh, curated, cool, and same day delivery flower bouquets. miuagtarsa nerafae kertyeraus.</p>
  </div>
  <div class="abs social"><span></span><span></span><span></span></div>
  <div class="abs f-col reach">
    <h3>Reach Brisa</h3>
    <ul>
      <li><svg width="16" height="22" viewBox="0 0 16 22"><path d="M8 0a8 8 0 0 0-8 8c0 6 8 14 8 14s8-8 8-14a8 8 0 0 0-8-8z" fill="#fff"/><circle cx="8" cy="8" r="3" fill="#3b3b3b"/></svg><span>2210 Arbor Lane<br>San Diego, CA 92104</span></li>
      <li><svg width="22" height="15" viewBox="0 0 22 15"><rect x="1" y="1" width="20" height="13" fill="none" stroke="#fff" stroke-width="1.8"/><path d="M1 1l10 8 10-8" fill="none" stroke="#fff" stroke-width="1.8"/></svg><span>info@brisapetals.com</span></li>
      <li><svg width="18" height="18" viewBox="0 0 18 18"><path d="M4 1l3 4-2 2c1 3 3 5 6 6l2-2 4 3-2 3C8 17 1 10 1 3z" fill="#fff"/></svg><span>555-014-2290</span></li>
    </ul>
  </div>
  <div class="abs f-col newsletter">
    <h3>Newsletter</h3>
    <p>We promise to only send you good things like discounts!</p>
    <form class="subscribe"><input type="email" aria-label="Email address"><button type="button">SUBMIT</button></form>
  </div>
  <div class="abs f-wavy"></div>
  <nav class="abs f-links"><a href="#">Terms and Conditions</a> | <a href="#">Privacy Policy</a> | <a href="#">Site Map</a></nav>
  <p class="abs f-copy">Copyright © 2013. All Rights Reserved.</p>
</footer>

</body>
</html>
```